Flyer Design Project - Pebblefern Meditation

I require a flyer to be created for a course. It is a meditation course. So I want the cover design to look quirky but calm.

I have attached a previous design. This project is for Pebblefern meditation. Although I have attached the previous flyer for guidance of the lay out and words used, I DO NOT want to to be a direct copy, I want it to look completely different. SO be creative. Any copies or anything that looks close to a copy will not even be considered.

I want the flyer to be A5 side but also the ability to resize it onto smaller cards.

If you need further information about the design brief please contact me.

Target Market(s)

20 to 40 year olds

Requirements
Must have
• Must have space for a logo which is currently being designed by the pixel bazaar. For the time being insert the tall willow lane wellness logo which is attached.

Picture something related to cupcakes on the front and course detail on the back same as the attached sample.
Should not have
• a direct copy of my samples I have attached.

```html
<!DOCTYPE html>
<html lang="en">
<head>
<meta charset="utf-8">
<title>Pebblefern Meditation Course Flyer – Front and Back</title>
<link rel="stylesheet" href="https://fonts.googleapis.com/css2?family=Fraunces:wght@600;700&family=Nunito:wght@400;600;700;800&display=swap">
<style>
  :root {
    --sage: #dfe7dc;
    --sage-deep: #8aa596;
    --cream: #fbf7f1;
    --cocoa: #4a3530;
    --cocoa-soft: #6b5550;
    --apricot: #e9793a;
    --blush: #f3d6c8;
    --sheet: #e9e3da;
  }
  * { margin: 0; padding: 0; box-sizing: border-box; }
  html, body { width: 846px; height: 1200px; overflow: hidden; background: var(--sheet); }
  body { font-family: "Nunito", Arial, sans-serif; color: var(--cocoa); }

  .sheet { position: relative; width: 846px; height: 1200px; }

  /* ---------- Front ---------- */
  .front {
    position: absolute; left: 0; top: 0; width: 846px; height: 594px;
    background: var(--sage); overflow: hidden;
  }
  .front__hero {
    position: absolute; left: 420px; top: 70px; width: 400px; height: 400px; border-radius: 50%;
    background:
      radial-gradient(circle at 50% 38%, #fff8f0 0%, #f6dcc6 30%, transparent 52%),
      radial-gradient(ellipse 60% 40% at 50% 78%, #7a4e3c 0%, #9b6a52 55%, transparent 80%),
      radial-gradient(circle at 50% 50%, #f1c9ac 0%, #e7b494 70%, #d9a282 100%);
  }
  .front__ring {
    position: absolute; left: 400px; top: 50px; width: 440px; height: 440px;
    border-radius: 50%; border: 2px dashed var(--sage-deep);
  }
  .front__kicker {
    position: absolute; left: 56px; top: 70px;
    font-size: 13px; font-weight: 800; letter-spacing: 3px; text-transform: uppercase; color: var(--sage-deep);
  }
  .front__title {
    position: absolute; left: 52px; top: 100px; width: 360px;
    font-family: "Fraunces", Georgia, serif; font-weight: 700;
    font-size: 60px; line-height: 68px; color: var(--cocoa);
  }
  .front__tagline {
    position: absolute; left: 56px; top: 330px; width: 330px;
    font-size: 22px; line-height: 30px; font-weight: 800; color: var(--apricot);
  }
  .front__maker {
    position: absolute; left: 56px; top: 510px;
    display: flex; align-items: center; gap: 12px;
    font-size: 15px; font-weight: 700; color: var(--cocoa);
  }
  .front__maker-dot { width: 30px; height: 30px; border-radius: 50%; background: var(--cocoa); }
  .front__side {
    position: absolute; right: 26px; top: 520px;
    font-size: 13px; font-weight: 700; letter-spacing: 2px; text-transform: uppercase; color: var(--sage-deep);
  }

  /* ---------- Back ---------- */
  .back {
    position: absolute; left: 0; top: 606px; width: 846px; height: 594px;
    background: var(--cream); display: flex; flex-direction: column;
  }
  .back__body { flex: 1; display: flex; gap: 40px; padding: 34px 48px 0 48px; }
  .back__col { display: flex; flex-direction: column; gap: 10px; }
  .back__col--story { width: 380px; }
  .back__col--offer { width: 330px; }

  .heading {
    font-family: "Fraunces", Georgia, serif; font-weight: 700;
    font-size: 24px; line-height: 30px; color: var(--cocoa);
  }
  .heading--spaced { margin-top: 12px; font-size: 20px; line-height: 26px; }
  .copy { font-size: 15px; line-height: 22px; color: var(--cocoa-soft); }
  .accent { color: var(--apricot); font-weight: 700; }

  .perks { list-style: none; display: flex; flex-direction: column; gap: 9px; margin-top: 4px; }
  .perks li { display: flex; gap: 10px; font-size: 15px; line-height: 22px; color: var(--cocoa-soft); }
  .perks svg { flex: none; margin-top: 3px; }

  .back__footer {
    height: 92px; background: var(--cocoa); color: var(--cream);
    display: flex; align-items: center; justify-content: space-between; padding: 0 48px;
  }
  .maker { display: flex; align-items: center; gap: 12px; }
  .maker__square { width: 34px; height: 34px; background: var(--blush); }
  .maker__text { font-size: 13px; line-height: 18px; font-weight: 600; }
  .maker__name { display: block; font-size: 16px; font-weight: 800; }
  .contact { text-align: right; font-size: 17px; line-height: 26px; font-weight: 800; }
  .contact__web { color: var(--blush); }
</style>
</head>
<body>
<main class="sheet">

  <section class="front" aria-label="Front of flyer">
    <div class="front__ring"></div>
    <div class="front__hero" role="img" aria-label="Photograph of a single frosted cupcake in a chocolate paper case, seen from above"></div>
    <p class="front__kicker">A mindful eating course</p>
    <h1 class="front__title">Pebblefern Meditation Course</h1>
    <p class="front__tagline">Learn to eat a cupcake without gaining weight!</p>
    <div class="front__maker">
      <span class="front__maker-dot"></span>
      <span>Tall Willow Lane Wellness</span>
    </div>
    <p class="front__side">Front</p>
  </section>

  <section class="back" aria-label="Back of flyer">
    <div class="back__body">
      <div class="back__col back__col--story">
        <h2 class="heading">Cupcake what?!</h2>
        <p class="copy">Yes you read right. <span class="accent">Pebblefern meditation!</span> What could be better than combining the delectable taste of a yummy cupcake with meditation, right? Well that is exactly what this course is all about, with a little bit of mindfulness thrown in.</p>
        <h2 class="heading heading--spaced">“I already know how to eat cupcakes.”</h2>
        <p class="copy">We challenge you that you have in fact not really eaten a cupcake. So we are going to teach you how to do it mindfully, savouring every bite, so a sweet treat becomes a calm moment.</p>
      </div>

      <div class="back__col back__col--offer">
        <h2 class="heading">What you get</h2>
        <ul class="perks">
          <li><svg width="16" height="16" viewBox="0 0 16 16" aria-hidden="true"><circle cx="8" cy="8" r="8" fill="#8aa596"/><path d="M4.5 8.2l2.3 2.3 4.7-4.8" fill="none" stroke="#fff" stroke-width="2" stroke-linecap="round" stroke-linejoin="round"/></svg><span>A Pebblefern Meditation course book</span></li>
          <li><svg width="16" height="16" viewBox="0 0 16 16" aria-hidden="true"><circle cx="8" cy="8" r="8" fill="#8aa596"/><path d="M4.5 8.2l2.3 2.3 4.7-4.8" fill="none" stroke="#fff" stroke-width="2" stroke-linecap="round" stroke-linejoin="round"/></svg><span>Mindfulness and meditation instruction online</span></li>
          <li><svg width="16" height="16" viewBox="0 0 16 16" aria-hidden="true"><circle cx="8" cy="8" r="8" fill="#8aa596"/><path d="M4.5 8.2l2.3 2.3 4.7-4.8" fill="none" stroke="#fff" stroke-width="2" stroke-linecap="round" stroke-linejoin="round"/></svg><span>Learn how to eat a cupcake mindfully</span></li>
          <li><svg width="16" height="16" viewBox="0 0 16 16" aria-hidden="true"><circle cx="8" cy="8" r="8" fill="#8aa596"/><path d="M4.5 8.2l2.3 2.3 4.7-4.8" fill="none" stroke="#fff" stroke-width="2" stroke-linecap="round" stroke-linejoin="round"/></svg><span>Meditation techniques and postures</span></li>
          <li><svg width="16" height="16" viewBox="0 0 16 16" aria-hidden="true"><circle cx="8" cy="8" r="8" fill="#e9793a"/><path d="M4.5 8.2l2.3 2.3 4.7-4.8" fill="none" stroke="#fff" stroke-width="2" stroke-linecap="round" stroke-linejoin="round"/></svg><span><span class="accent">FREE</span> mp3 guided meditation download</span></li>
          <li><svg width="16" height="16" viewBox="0 0 16 16" aria-hidden="true"><circle cx="8" cy="8" r="8" fill="#8aa596"/><path d="M4.5 8.2l2.3 2.3 4.7-4.8" fill="none" stroke="#fff" stroke-width="2" stroke-linecap="round" stroke-linejoin="round"/></svg><span>5% of the course goes to charity – see our website for this month’s cause</span></li>
        </ul>
      </div>
    </div>

    <footer class="back__footer">
      <div class="maker">
        <span class="maker__square"></span>
        <p class="maker__text">Brought to you by<span class="maker__name">Tall Willow Lane Wellness</span></p>
      </div>
      <div class="contact">
        <p>Phone (02) 5550 1847</p>
        <p class="contact__web">www.pebblefern-calm.com.au</p>
      </div>
    </footer>
  </section>

</main>
</body>
</html>
```